Copper Vale Tattoo

Business card / Appointment card in one

Ive attached the new logo along with a simple format of what I would like written out on the back! Would like a clean/ modern style font to be used! I also attached the current card for a reference of style!

The colors of this would be either white and gold lettering or black with gold lettering.

Email - CopperValeNB@inkmail.example
Ph # 555-482-9073

The message at bottom of back - All cancellations or No Call No Shows within 48 hours of appointment time will result in a forfeit of deposit.

Small block avail (if card is black) to write in appointment date/time

Target Market(s)

Card for Tattoo shop

Contact Information for Business Card

in project description area!

Font styles to use
Sans Serif

Requirements
Must have
• Please refer to current business card photos that were attached as well!
Nice to have
• Looking for blacks, greys and gold for color scheme

```html
<!DOCTYPE html>
<html lang="en">
<head>
<meta charset="utf-8">
<title>Copper Vale Tattoo – Business &amp; Appointment Card</title>
<link rel="stylesheet" href="https://fonts.googleapis.com/css2?family=Arimo:wght@700&family=Lato:wght@400&display=swap">
<style>
  :root {
    --backdrop: #8f8f8f;
    --card-black: #222222;
    --gold: #fbb827;
    --gold-soft: #f7c631;
    --policy-grey: #c9c9c9;
    --rule-grey: #6a6a6a;
    --slip-white: #efefef;
    --slip-ink: #1e1e1e;
  }
  * { margin: 0; padding: 0; box-sizing: border-box; }
  html, body {
    width: 1200px;
    height: 1200px;
    overflow: hidden;
    background: var(--backdrop);
  }
  .canvas {
    position: relative;
    width: 1200px;
    height: 1200px;
  }
  .card {
    position: absolute;
    top: 310px;
    height: 595px;
    background: var(--card-black);
    box-shadow: 2px 3px 6px rgba(0, 0, 0, 0.35);
    overflow: hidden;
  }
  .card--front {
    left: 234px;
    width: 364px;
    display: flex;
    align-items: center;
    justify-content: center;
  }
  .front-name {
    font-family: "Arimo", Arial, sans-serif;
    font-weight: 700;
    font-size: 44px;
    line-height: 1.15;
    color: var(--gold);
    text-align: center;
  }
  .card--back {
    left: 627px;
    width: 370px;
    text-align: center;
  }
  .studio-name {
    position: absolute;
    top: 408px;
    left: 0;
    right: 0;
    font-family: "Arimo", Arial, sans-serif;
    font-weight: 700;
    font-size: 38px;
    color: var(--gold);
    top: 98px;
  }
  .contact {
    position: absolute;
    top: 218px;
    left: 0;
    right: 0;
    font-family: "Lato", Arial, sans-serif;
    font-size: 21px;
    line-height: 30px;
    color: var(--gold-soft);
  }
  .divider {
    position: absolute;
    top: 307px;
    left: 34px;
    width: 302px;
    height: 1px;
    background: var(--rule-grey);
  }
  .policy {
    position: absolute;
    top: 331px;
    left: 0;
    right: 0;
    font-family: "Lato", Arial, sans-serif;
    font-size: 17px;
    line-height: 22.5px;
    color: var(--policy-grey);
  }
  .appointment-slip {
    position: absolute;
    top: 443px;
    left: 0;
    right: 0;
    bottom: 0;
    background: var(--slip-white);
    padding: 40px 0 0 79px;
    text-align: left;
    font-family: "Lato", Arial, sans-serif;
    font-size: 16px;
    color: var(--slip-ink);
  }
  .slip-field {
    display: flex;
    align-items: baseline;
    height: 35px;
  }
  .slip-line {
    display: inline-block;
    width: 166px;
    border-bottom: 1px solid var(--slip-ink);
    margin-left: 2px;
  }
</style>
</head>
<body>
<main class="canvas">
  <section class="card card--front" aria-label="Card front">
    <p class="front-name">Copper<br>Vale<br>Tattoo</p>
  </section>

  <section class="card card--back" aria-label="Card back">
    <h1 class="studio-name">Copper Vale Tattoo</h1>
    <p class="contact">
      555-482-9073<br>
      CopperValeNB@inkmail.example
    </p>
    <div class="divider"></div>
    <p class="policy">
      All cancellations or No Call No Shows<br>
      within 48 hours of<br>
      appointment time will result<br>
      in a forfeit of deposit.
    </p>
    <div class="appointment-slip">
      <div class="slip-field">DATE<span class="slip-line"></span></div>
      <div class="slip-field">TIME<span class="slip-line"></span></div>
    </div>
  </section>
</main>
</body>
</html>
```